Spice Mix Label Bottle Branding - Health and Weight Loss Mixes

The company is called ZestRow Spice Mix's. We've created 5 spice mixes using ingredients that promote health and weight loss. We already have a logo but now we need labels for our bottles. We would like to see designs that have the feel of health supplements (see attached examples)

We would like a different colour featured with each of our flavours.

Our flavours are:
-Golden Chai (Yellow)
-Mild Curry (Orange)
-Coffee Rub (brown)
-Garlic Oregano (Green)
-Taco (Blue)

Thank you!

Target Market(s)

Ages 22-35. Men and Female. Trendy, Hipster.

Industry/Entity Type

Food Production

Font styles to use
Sans Serif

Colors
f37122
0655a3
0692cd
9bcb3c
fbee3f

Requirements
Must have
• A different featured colour for each flavour.
• The ZestRow Spices Logo (attached)
• The slogan: "Weight Loss Ingredients"
• -Golden Chai (Yellow)
• -Mild Curry (Orange)
• -Coffee Rub (brown)
• -Garlic Oregano (Green)
• -Taco (Blue)
• Text Files attached.
Nice to have
• A black label with a featured colour for each of the spice mice flavours.
• 'No Salt added'

```html
<!DOCTYPE html>
<html lang="en">
<head>
<meta charset="utf-8">
<title>ZestRow Spices – Taco Label</title>
<link rel="stylesheet" href="https://fonts.googleapis.com/css2?family=Oswald:wght@500;600&family=Montserrat:wght@700&display=swap">
<style>
  :root {
    --label-black: #000000;
    --taco-blue: #3a78b5;
    --taco-blue-deep: #1d4f86;
    --ink-white: #ffffff;
  }
  html, body {
    margin: 0;
    padding: 0;
    width: 1200px;
    height: 1200px;
    overflow: hidden;
    background: var(--label-black);
  }
  .label {
    display: block;
    width: 1200px;
    height: 1200px;
  }
  .flavour-name,
  .claim {
    font-family: "Oswald", sans-serif;
    font-weight: 500;
    fill: var(--ink-white);
  }
  .flavour-name { font-size: 54px; letter-spacing: 10px; }
  .claim { font-size: 44px; letter-spacing: 4px; }
  .brand-name {
    font-family: "Oswald", sans-serif;
    font-weight: 600;
    fill: var(--ink-white);
  }
  .brand-word { font-size: 150px; }
  .brand-sub { font-size: 38px; letter-spacing: 22px; }
  .slogan {
    font-family: "Montserrat", sans-serif;
    font-weight: 700;
    font-size: 31px;
    fill: var(--ink-white);
  }
  .rule { stroke: var(--ink-white); stroke-width: 2; }
  .rule-dot { fill: var(--ink-white); }
</style>
</head>
<body>
<svg class="label" viewBox="0 0 1200 1200" xmlns="http://www.w3.org/2000/svg">
  <defs>
    <radialGradient id="burst-glow" cx="600" cy="600" r="540" gradientUnits="userSpaceOnUse">
      <stop offset="0.55" stop-color="#3a78b5"/>
      <stop offset="0.78" stop-color="#2a5f96"/>
      <stop offset="1" stop-color="#000000"/>
    </radialGradient>
    <path id="arc-top" d="M 350 600 A 250 250 0 0 1 850 600"/>
    <path id="arc-bottom" d="M 310 600 A 290 290 0 0 0 890 600"/>
  </defs>

  <rect class="backdrop" width="1200" height="1200" fill="var(--label-black)"/>

  <circle class="burst" cx="600" cy="600" r="540" fill="url(#burst-glow)" role="img" aria-label="Blue sunburst rays radiating around the label badge"/>

  <circle class="badge" cx="600" cy="600" r="335" fill="var(--label-black)"/>

  <text class="flavour-name" text-anchor="middle">
    <textPath href="#arc-top" startOffset="50%">TACO</textPath>
  </text>

  <line class="rule" x1="345" y1="480" x2="855" y2="480"/>
  <circle class="rule-dot" cx="345" cy="480" r="5"/>
  <circle class="rule-dot" cx="855" cy="480" r="5"/>

  <text class="brand-name brand-word" x="600" y="650" text-anchor="middle">ZestRow</text>
  <text class="brand-name brand-sub" x="611" y="712" text-anchor="middle">SPICES</text>

  <text class="slogan" x="600" y="760" text-anchor="middle">Weight Loss Ingredients</text>
  <line class="rule" x1="425" y1="775" x2="775" y2="775"/>
  <circle class="rule-dot" cx="588" cy="788" r="4"/>
  <circle class="rule-dot" cx="600" cy="788" r="4"/>
  <circle class="rule-dot" cx="612" cy="788" r="4"/>

  <text class="claim" text-anchor="middle">
    <textPath href="#arc-bottom" startOffset="50%">NO SALT ADDED</textPath>
  </text>
</svg>
</body>
</html>
```